Upmarket Dessert Lounge needs a Business Card Design

We are an upmarket dessert lounge needing a business card to match our image.

We want something that is simple yet beautiful, feminine, classy, sophisticated and elegant. We want it to stand out and don't mind if it is bold.

The design should include our logo and colours of red or maroon with gold highlights. We don't mind if black is used.

Marlow & Quince

Target Market(s)

For those who like to indulge or treat themselves and give in to their temptations on good quality desserts.

Industry/Entity Type

Business

Requirements
Must have
• Must include our logo and our name

Marlow & Quince

M & Q

```html
<!DOCTYPE html>
<html lang="en">
<head>
<meta charset="utf-8">
<title>Marlow &amp; Quince — Business Card</title>
<link rel="stylesheet" href="https://fonts.googleapis.com/css2?family=Cinzel:wght@500&family=Open+Sans:wght@400&display=swap">
<style>
  :root {
    --backdrop: #d9d6d2;
    --maroon-deep: #6e1216;
    --maroon: #9a2024;
    --maroon-glow: #b02a2c;
    --gold: #e2b877;
    --gold-soft: #f0cf98;
    --copper-dark: #8a3a1c;
    --copper-light: #f3b582;
    --white: #ffffff;
  }
  * { margin: 0; padding: 0; box-sizing: border-box; }
  html, body {
    width: 1200px;
    height: 951px;
    overflow: hidden;
    background: var(--backdrop);
  }
  .canvas {
    position: relative;
    width: 1200px;
    height: 951px;
  }
  .card {
    position: absolute;
    width: 720px;
    height: 412px;
    border-radius: 26px;
    overflow: hidden;
    background: radial-gradient(ellipse at 40% 45%, var(--maroon-glow) 0%, var(--maroon) 45%, var(--maroon-deep) 100%);
    box-shadow: 0 14px 30px rgba(0, 0, 0, 0.28);
  }
  .card-front { left: 90px; top: 50px; }
  .card-back { left: 390px; top: 490px; }

  .edge-band {
    position: absolute;
    top: 0;
    width: 16px;
    height: 100%;
    background: linear-gradient(180deg, var(--copper-dark) 0%, var(--copper-light) 30%, var(--copper-dark) 55%, var(--copper-light) 80%, var(--copper-dark) 100%);
  }
  .edge-band.left { left: 0; }
  .edge-band.right { right: 0; }

  .wordmark {
    font-family: "Cinzel", serif;
    font-weight: 500;
    color: var(--gold);
    letter-spacing: 0.04em;
    white-space: nowrap;
  }
  .card-front .wordmark {
    position: absolute;
    left: 0; right: 0;
    top: 128px;
    text-align: center;
    font-size: 46px;
  }
  .website {
    position: absolute;
    left: 0; right: 0;
    top: 296px;
    text-align: center;
    font-family: "Open Sans", sans-serif;
    font-size: 19px;
    letter-spacing: 0.12em;
    color: var(--gold);
  }

  .card-back .monogram {
    position: absolute;
    left: 44px;
    top: 150px;
    width: 240px;
    text-align: center;
    font-size: 56px;
  }
  .contact {
    position: absolute;
    right: 46px;
    top: 116px;
    text-align: right;
    font-family: "Open Sans", sans-serif;
    color: var(--white);
  }
  .contact .business-name {
    font-size: 25px;
    color: var(--gold-soft);
    margin-bottom: 20px;
  }
  .contact .address,
  .contact .phone,
  .contact .email {
    font-size: 19px;
    line-height: 1.3;
  }
  .contact .phone { margin-top: 20px; }
</style>
</head>
<body>
  <main class="canvas">
    <section class="card card-front" aria-label="Business card front">
      <span class="edge-band left"></span>
      <span class="edge-band right"></span>
      <div class="wordmark">MARLOW &amp; QUINCE</div>
      <p class="website">www.marlow&amp;quince.com</p>
    </section>

    <section class="card card-back" aria-label="Business card back">
      <span class="edge-band right"></span>
      <div class="wordmark monogram">M&amp;Q</div>
      <div class="contact">
        <p class="business-name">Marlow &amp; Quince</p>
        <p class="address">48 Linden Street, Suite 300<br>Harbor City, New York 10021</p>
        <p class="phone">555-214-7380</p>
        <p class="email">info@marlow&amp;quince.com</p>
      </div>
    </section>
  </main>
</body>
</html>
```